CREATE A KILLER WEBSITE DESIGN

We are a firearms training company that trains CIVILIANS (no police or military pictures - thank you!) to defend themselves and are looking for a killer design that's clean, easy to navigate and modern! We want the newest trends applied to this sight like a scrollable site so you can scroll down and see all the features. We are okay with tweaking the HTML but need the artistic design to look good. I'll provide a link to our current site along with a sight we really like so you can get an idea!

I'm supplying a PowerPoint Design we are going with from another designer so you can match the style to the new site.

PAGES: (Please use information from our current site. We like the information but just want a more polished look similar to the NWDFA site below but in our colors.)
Home - Long Form Scrolling Site. Top fold will be a video with a play button.
Falconry Institute - Seven Level Training Program Info Page That Will Contain A Video.
Contact Us - This will be a page that DOES NOT CONTAIN AN EMAIL ADDRESS. Just a contact us form
Meet The Trainer: Brendan Osterlow

Our site:
https://www.brightharborguarding.biz

Sights We Like:
https://www.nwdefenderalliance.com
https://quorvel.com
https://brinmoreworkscorp.com
https://www.pelldrivegear.com

Target Market(s)

Men and women ages 21 to 100 years old

Industry/Entity Type

Self Defense

Number of Pages Required

5+ page

Font styles to use
Sans Serif

Colors
f26267

Requirements
Must have
• Clean and engaging. Use of colors that match our logo.
Should not have
• Poor design quality

```html
<!DOCTYPE html>
<html lang="en">
<head>
<meta charset="utf-8">
<title>Bright Harbor Guarding – Firearms Training</title>
<link rel="stylesheet" href="https://fonts.googleapis.com/css2?family=Audiowide&family=Lato:ital,wght@0,400;0,700;0,900;1,400&display=swap">
<style>
:root{
  --red:#d71e2b;
  --red-dark:#b8101d;
  --black:#0c0c0c;
  --ink:#1a1a1a;
  --grey-bg:#efefef;
  --text:#3a3a3a;
  --muted:#6a6a6a;
  --white:#ffffff;
}
*{box-sizing:border-box;margin:0;padding:0}
html,body{width:1200px;height:5004px;overflow:hidden}
body{position:relative;background:var(--white);font-family:"Lato",sans-serif;color:var(--text)}
.display{font-family:"Audiowide",sans-serif;text-transform:uppercase;letter-spacing:1px}
section,header,footer{position:absolute;left:0;width:1200px}
.abs{position:absolute}
.red{color:var(--red)}
.btn{position:absolute;display:flex;align-items:center;justify-content:center;font-family:"Audiowide",sans-serif;text-transform:uppercase;font-size:12px;letter-spacing:1px;border-radius:6px}
.target{position:absolute;width:38px;height:38px}

/* header */
.site-header{top:0;height:120px;background:var(--white)}
.brand{left:161px;top:30px;display:flex;align-items:center;gap:10px}
.brand-mark{width:22px;height:22px;border-radius:50%;background:var(--red)}
.brand-name{font-family:"Audiowide",sans-serif;font-size:15px;color:var(--ink);line-height:1.15;text-transform:uppercase;width:130px}
.topbar{left:600px;top:0;width:439px;height:35px}
.login{left:505px;top:8px;font-size:13px;color:var(--ink);display:flex;align-items:center;gap:8px}
.login i{width:26px;height:26px;border-radius:50%;background:var(--red);display:inline-block}
.phone-top{left:645px;top:9px;font-size:13px;color:var(--white);display:flex;align-items:center;gap:10px}
.search{left:839px;top:0;width:200px;height:35px;background:#2b2b2b;color:#bbb;font-size:12px;padding:11px 14px}
.nav{top:68px;font-size:14px;color:var(--ink)}
.nav-active{left:502px;top:112px;width:44px;height:6px;background:var(--ink)}
.btn-trainer{left:835px;top:58px;width:204px;height:39px;border:2px solid var(--red);color:var(--red);background:var(--white)}

/* hero */
.hero{top:120px;height:580px}
.hero h1{left:161px;top:160px;color:var(--white);font-size:29px;line-height:1.2;font-weight:400}
.hero p{left:163px;top:235px;width:370px;color:#e6e6e6;font-size:16px;line-height:1.6}
.btn-tickets{left:163px;top:313px;width:150px;height:41px;background:var(--red);color:var(--white)}
.btn-academy{left:326px;top:313px;width:205px;height:41px;border:2px solid var(--white);color:var(--white)}

/* about */
.about{top:700px;height:558px}
.about-eyebrow{left:627px;top:124px;font-size:16px;color:var(--ink)}
.about h2{left:627px;top:148px;font-size:33px;color:var(--ink);font-weight:400}
.about-copy{left:627px;top:193px;width:410px;font-size:13px;line-height:27px;text-align:justify;color:var(--text)}
.btn-meet{left:627px;top:432px;width:286px;height:41px;border:2px solid var(--red);color:var(--red)}

/* levels */
.levels{top:1258px;height:1049px;background:var(--grey-bg)}
.section-title{width:1200px;text-align:center;font-size:34px;color:var(--ink);font-weight:400;line-height:1.2}
.levels-intro{left:160px;top:226px;width:880px;text-align:center;font-size:15px;line-height:29px;color:var(--ink)}
.card{position:absolute;width:424px;height:133px;background:var(--white);box-shadow:0 2px 8px rgba(0,0,0,.08)}
.card .num{position:absolute;left:20px;top:22px;font-family:"Audiowide",sans-serif;font-size:48px;color:transparent;-webkit-text-stroke:2px var(--red);line-height:1}
.card h3{position:absolute;left:91px;top:26px;font-family:"Audiowide",sans-serif;text-transform:uppercase;font-size:14px;color:var(--ink);font-weight:400;letter-spacing:.5px}
.card p{position:absolute;left:91px;top:52px;width:305px;font-size:12.5px;line-height:22px;text-align:justify;color:var(--text)}
.levels-brand{left:720px;top:880px;width:220px;text-align:center;font-family:"Audiowide",sans-serif;font-size:17px;color:var(--red);line-height:1.2;text-transform:uppercase}

/* videos */
.videos{top:2307px;height:790px;background:var(--black)}
.videos .section-title{color:var(--white)}
.video-frame{left:161px;top:184px;width:878px;height:447px;border:6px solid var(--white);border-radius:14px;overflow:hidden}
.btn-learn{left:455px;top:670px;width:290px;height:45px;border:2px solid var(--red);color:var(--red)}

/* success */
.success{top:3097px;height:523px;background:var(--grey-bg)}
.avatar{left:555px;top:192px;width:90px;height:90px;border-radius:50%;border:3px solid var(--red);background:var(--white)}
.quote{left:200px;top:296px;width:800px;text-align:center;font-style:italic;font-size:15px;line-height:27px;color:var(--ink)}
.quote-name{left:0;top:358px;width:1200px;text-align:center;font-weight:700;font-size:17px;color:var(--ink)}
.quote-date{left:0;top:386px;width:1200px;text-align:center;font-size:13px;color:var(--ink)}
.arrow-btn{top:296px;width:34px;height:34px;border-radius:50%;border:1.5px solid #444;display:flex;align-items:center;justify-content:center;font-size:16px;color:#333}
.dots{left:568px;top:438px;display:flex;gap:9px}
.dots i{width:9px;height:9px;border-radius:50%;background:#ccc;display:block}
.dots i.on{background:var(--red)}

/* press */
.press{top:3620px;height:353px;background:var(--white)}
.press-box{position:absolute;top:180px;width:192px;height:98px;background:var(--white);box-shadow:0 2px 10px rgba(0,0,0,.12);display:flex;align-items:center;justify-content:center;font-family:"Lato",sans-serif;font-weight:900;font-size:22px;color:var(--ink)}

/* touch */
.touch{top:3973px;height:451px;background:#1b1b1b}
.touch .section-title{color:var(--white)}
.field{position:absolute;background:var(--white);border:1px solid #ccc;font-size:12px;color:#777;padding:7px 12px}
.btn-submit{left:517px;top:342px;width:165px;height:41px;border:2px solid var(--white);color:var(--white)}

/* contact */
.contact{top:4424px;height:580px;background:var(--white)}
.contact h2{left:612px;top:103px;font-size:31px;color:var(--ink);font-weight:400}
.pin{position:absolute;width:38px;height:38px;border-radius:50%;background:var(--red);display:flex;align-items:center;justify-content:center}
.c-label{position:absolute;font-size:15px;font-weight:700;color:var(--ink)}
.c-value{position:absolute;font-size:13px;color:var(--ink)}
.copyright{left:161px;top:542px;font-size:13px;color:var(--white)}
.social{position:absolute;top:539px;width:28px;height:28px;border-radius:50%;border:2px solid var(--red);background:var(--white)}
</style>
</head>
<body>

<header class="site-header">
  <div class="abs brand"><span class="brand-mark"></span><span class="brand-name">Bright Harbor Guarding</span></div>
  <svg class="abs topbar" width="439" height="35" viewBox="0 0 439 35"><path d="M0 0H439V35H18Z" fill="#0c0c0c"/></svg>
  <div class="abs login"><i></i>Log In</div>
  <div class="abs phone-top">
    <svg width="24" height="24" viewBox="0 0 24 24"><circle cx="12" cy="12" r="11" fill="none" stroke="#fff" stroke-width="1.5"/><path d="M8.5 7c.6-.4 1.2-.3 1.5.3l.9 1.8c.2.5 0 1-.4 1.3l-.7.5c.6 1.4 1.6 2.4 3 3l.5-.7c.3-.4.8-.6 1.3-.4l1.8.9c.6.3.7.9.3 1.5-.8 1.2-2 1.6-3.4 1-2.6-1.1-4.5-3-5.6-5.6-.6-1.4-.2-2.6 1-3.4z" fill="#fff"/></svg>
    Call - 555-0142-BHG</div>
  <div class="abs search">Search
    <svg class="abs" style="right:14px;top:11px" width="13" height="13" viewBox="0 0 13 13"><circle cx="5.5" cy="5.5" r="4" fill="none" stroke="#fff" stroke-width="2"/><path d="M8.5 8.5L12 12" stroke="#fff" stroke-width="2"/></svg></div>
  <div class="abs nav" style="left:505px">Home</div>
  <div class="abs nav" style="left:584px">Falconry Institute</div>
  <div class="abs nav" style="left:724px">Contact Us</div>
  <div class="abs nav-active"></div>
  <div class="btn btn-trainer">Meet The Trainer</div>
</header>

<section class="hero">
  <svg class="abs" style="left:0;top:0" width="1200" height="580" viewBox="0 0 1200 580">
    <rect width="1200" height="460" fill="#0c0c0c"/>
    <path d="M0 455C220 560 520 580 700 560C900 535 1060 480 1200 420V0H0Z" fill="#0c0c0c"/>
    <path d="M0 455C220 560 520 580 700 560C900 535 1060 480 1200 420V455C1060 520 900 565 700 580C500 595 220 575 0 490Z" fill="#d71e2b"/>
    <path d="M710 0C640 120 630 330 745 520C900 520 1060 470 1200 410V0Z" fill="#b8101d"/>
    <path d="M722 0C655 120 648 320 760 505C910 500 1060 455 1200 396V0Z" fill="#6e6e6e" role="img" aria-label="Photo of a civilian student aiming a handgun at an indoor range"/>
    <circle cx="938" cy="263" r="36" fill="#fff"/>
    <circle cx="938" cy="263" r="26" fill="none" stroke="#d71e2b" stroke-width="3"/>
    <path d="M930 249L952 263L930 277Z" fill="#d71e2b"/>
  </svg>
  <h1 class="abs display">We are a firearms<br>training company</h1>
  <p class="abs">Providing Training to CIVILIANS To Deefend Themselves</p>
  <div class="btn btn-tickets">Get Tickets</div>
  <div class="btn btn-academy">Falconry Institute</div>
</section>

<section class="about">
  <svg class="abs" style="left:105px;top:0" width="460" height="440" viewBox="0 0 460 440"><path d="M230 0L460 430H0Z" fill="#d71e2b" opacity=".08"/></svg>
  <div class="abs" style="left:165px;top:71px;width:408px;height:408px;border-radius:50%;border:5px solid var(--red);background:linear-gradient(160deg,#9a9a9a,#4a4a4a)" role="img" aria-label="Black and white portrait of instructor Brendan Osterlow"></div>
  <svg class="target" style="left:628px;top:79px" viewBox="0 0 38 38"><circle cx="19" cy="19" r="17" fill="none" stroke="#d71e2b" stroke-width="3"/><circle cx="19" cy="19" r="11" fill="none" stroke="#d71e2b" stroke-width="3"/><circle cx="19" cy="19" r="5" fill="#d71e2b"/></svg>
  <div class="abs about-eyebrow">About The Instructor</div>
  <h2 class="abs display"><span class="red">Brendan</span> Osterlow</h2>
  <p class="abs about-copy">Brendan Osterlow is a 3rd generation Harbor City native and delighted to be a part of this great community. He is a true security expert with 25 years of experience in the security industry. He has appeared on Metro Wire, KRV One, Eastline &amp; Lakeside TV news outlets. He has been Featured in numerous publications and has trained thousands to protect themselves and their homes from thugs and thieves. He is certified by both the NSTA &amp; the NWDFA as a firearms instructor.</p>
  <div class="btn btn-meet">Meet The Brendan Osterlow</div>
</section>

<section class="levels">
  <svg class="target" style="left:581px;top:82px" viewBox="0 0 38 38"><circle cx="19" cy="19" r="17" fill="none" stroke="#d71e2b" stroke-width="3"/><circle cx="19" cy="19" r="11" fill="none" stroke="#d71e2b" stroke-width="3"/><circle cx="19" cy="19" r="5" fill="#d71e2b"/></svg>
  <h2 class="abs display section-title" style="top:127px">Our <span class="red">7 Levels</span> of training take<br>you from zero to <span class="red">hero</span></h2>
  <p class="abs levels-intro">Wanna hear something funny? Guess what the average person asks about a concealed weapons class? “How much is it and how long is it?” Can you believe it? We are talking about preparing you for life and death situations and the main concern is “How Fast” and “How Cheap?” WOW!</p>

  <div class="card" style="left:161px;top:344px"><span class="num">1</span><h3>Concealed Carry Class</h3><p>Lorem ipsum dolor sit amet, conse ctetuer adipiscing elit, sed diam nonummy nibh euismod tincidunt ut laoreet aliquam erat volutpat.</p></div>
  <div class="card" style="left:615px;top:344px"><span class="num">2</span><h3>Dynamic Defensive Shooting</h3><p>Lorem ipsum dolor sit amet, conse ctetuer adipiscing elit, sed diam nonummy nibh euismod tincidunt ut laoreet aliquam erat volutpat.</p></div>
  <div class="card" style="left:161px;top:509px"><span class="num">3</span><h3>Fine Tuning Your Technique</h3><p>Lorem ipsum dolor sit amet, conse ctetuer adipiscing elit, sed diam nonummy nibh euismod tincidunt ut laoreet aliquam erat volutpat.</p></div>
  <div class="card" style="left:615px;top:509px"><span class="num">4</span><h3>Virtual Threat-Lab</h3><p>Lorem ipsum dolor sit amet, conse ctetuer adipiscing elit, sed diam nonummy nibh euismod tincidunt ut laoreet aliquam erat volutpat.</p></div>
  <div class="card" style="left:161px;top:674px"><span class="num">5</span><h3>Tactical Skills &amp; Drills</h3><p>Lorem ipsum dolor sit amet, conse ctetuer adipiscing elit, sed diam nonummy nibh euismod tincidunt ut laoreet aliquam erat volutpat.</p></div>
  <div class="card" style="left:615px;top:674px"><span class="num">6</span><h3>Close Quarters Defense</h3><p>Lorem ipsum dolor sit amet, conse ctetuer adipiscing elit, sed diam nonummy nibh euismod tincidunt ut laoreet aliquam erat volutpat.</p></div>
  <div class="card" style="left:161px;top:839px"><span class="num">7</span><h3>Live Scenario Threat-Lab</h3><p>Lorem ipsum dolor sit amet, conse ctetuer adipiscing elit, sed diam nonummy nibh euismod tincidunt ut laoreet aliquam erat volutpat.</p></div>
  <div class="abs levels-brand">Bright Harbor<br>Guarding</div>
</section>

<section class="videos">
  <svg class="target" style="left:581px;top:74px" viewBox="0 0 38 38"><circle cx="19" cy="19" r="17" fill="none" stroke="#d71e2b" stroke-width="3"/><circle cx="19" cy="19" r="11" fill="none" stroke="#d71e2b" stroke-width="3"/><circle cx="19" cy="19" r="5" fill="#d71e2b"/></svg>
  <h2 class="abs display section-title" style="top:118px">Our Videos</h2>
  <div class="abs video-frame">
    <div style="position:absolute;inset:0;background:linear-gradient(120deg,#5a3a2a 0%,#3e4a4a 45%,#6a8a8c 75%,#2a2a2a 100%)" role="img" aria-label="Video still of a student practicing on a virtual shooting simulator"></div>
    <svg class="abs" style="left:397px;top:180px" width="72" height="72" viewBox="0 0 72 72"><circle cx="36" cy="36" r="34" fill="#d71e2b"/><path d="M28 22L52 36L28 50Z" fill="none" stroke="#fff" stroke-width="3"/></svg>
    <div class="abs" style="left:0;bottom:0;width:100%;height:30px;background:linear-gradient(transparent,rgba(0,0,0,.7))"></div>
    <svg class="abs" style="left:18px;bottom:10px" width="10" height="12" viewBox="0 0 10 12"><path d="M0 0L10 6L0 12Z" fill="#fff"/></svg>
    <div class="abs" style="left:60px;bottom:15px;width:760px;height:2px;background:rgba(255,255,255,.5)"></div>
  </div>
  <div class="btn btn-learn">Click here to learn more</div>
</section>

<section class="success">
  <svg class="target" style="left:581px;top:77px" viewBox="0 0 38 38"><circle cx="19" cy="19" r="17" fill="none" stroke="#d71e2b" stroke-width="3"/><circle cx="19" cy="19" r="11" fill="none" stroke="#d71e2b" stroke-width="3"/><circle cx="19" cy="19" r="5" fill="#d71e2b"/></svg>
  <h2 class="abs display section-title" style="top:120px">Success Stories</h2>
  <div class="abs avatar"></div>
  <p class="abs quote">“I had never held a gun when I took the Bright Harbor Guarding class and I’m hooked!<br>I’m going all the way to level 7! Thank you Bright Harbor Guarding!</p>
  <div class="abs quote-name">Marisa K.</div>
  <div class="abs quote-date">October 14, 2017</div>
  <div class="abs arrow-btn" style="left:113px">‹</div>
  <div class="abs arrow-btn" style="left:1051px">›</div>
  <div class="abs dots"><i></i><i class="on"></i><i></i><i></i></div>
</section>

<section class="press">
  <svg class="target" style="left:581px;top:77px" viewBox="0 0 38 38"><circle cx="19" cy="19" r="17" fill="none" stroke="#d71e2b" stroke-width="3"/><circle cx="19" cy="19" r="11" fill="none" stroke="#d71e2b" stroke-width="3"/><circle cx="19" cy="19" r="5" fill="#d71e2b"/></svg>
  <h2 class="abs display section-title" style="top:118px">As Seen On</h2>
  <div class="press-box" style="left:161px">Metro Wire</div>
  <div class="press-box" style="left:390px">Lakeside TV</div>
  <div class="press-box" style="left:618px">KRV One</div>
  <div class="press-box" style="left:847px">Eastline</div>
</section>

<section class="touch">
  <div class="abs" style="inset:0;background:linear-gradient(180deg,#2a2a2a,#111)" role="img" aria-label="Darkened photo of an indoor shooting range"></div>
  <svg class="target" style="left:581px;top:82px" viewBox="0 0 38 38"><circle cx="19" cy="19" r="17" fill="none" stroke="#fff" stroke-width="3"/><circle cx="19" cy="19" r="11" fill="none" stroke="#fff" stroke-width="3"/><circle cx="19" cy="19" r="5" fill="#fff"/></svg>
  <h2 class="abs display section-title" style="top:126px">Get In Touch</h2>
  <div class="field" style="left:247px;top:177px;width:343px;height:35px">Name*</div>
  <div class="field" style="left:247px;top:230px;width:343px;height:35px">Email*</div>
  <div class="field" style="left:247px;top:282px;width:343px;height:35px">Phone*</div>
  <div class="field" style="left:608px;top:177px;width:344px;height:140px">Message*</div>
  <div class="btn btn-submit">Submit Now</div>
</section>

<section class="contact">
  <svg class="abs" style="left:0;top:0" width="730" height="580" viewBox="0 0 730 580">
    <path d="M0 0H525L730 580H0Z" fill="#5a5a5a" role="img" aria-label="Black and white photo of a student with ear protection aiming a rifle outdoors"/>
  </svg>
  <svg class="target" style="left:544px;top:99px" viewBox="0 0 38 38"><circle cx="19" cy="19" r="17" fill="none" stroke="#d71e2b" stroke-width="3"/><circle cx="19" cy="19" r="11" fill="none" stroke="#d71e2b" stroke-width="3"/><circle cx="19" cy="19" r="5" fill="#d71e2b"/></svg>
  <h2 class="abs display">Contact Details</h2>
  <div class="pin" style="left:581px;top:191px"><svg width="16" height="20" viewBox="0 0 16 20"><path d="M8 0C3.6 0 0 3.4 0 7.6 0 13 8 20 8 20s8-7 8-12.4C16 3.4 12.4 0 8 0z" fill="#fff"/><circle cx="8" cy="7.5" r="3" fill="#d71e2b"/></svg></div>
  <div class="c-label" style="left:633px;top:192px">Harborline Office</div>
  <div class="c-value" style="left:633px;top:214px">P.O. Box 4410 , Cedar Point, FL 32990</div>
  <div class="pin" style="left:606px;top:268px"><svg width="18" height="18" viewBox="0 0 24 24"><path d="M6.6 2c.9-.6 1.8-.4 2.2.5l1.4 2.7c.3.7 0 1.5-.6 1.9l-1 .7c.9 2.1 2.4 3.6 4.5 4.5l.7-1c.4-.6 1.2-.9 1.9-.6l2.7 1.4c.9.4 1.1 1.3.5 2.2-1.2 1.8-3 2.4-5.1 1.5-3.9-1.6-6.8-4.5-8.4-8.4-.9-2.1-.3-3.9 1.2-5.4z" fill="#fff"/></svg></div>
  <div class="c-label" style="left:658px;top:270px">Phone</div>
  <div class="c-value" style="left:658px;top:292px">555-0142-BHG</div>
  <div class="pin" style="left:635px;top:346px"><svg width="18" height="18" viewBox="0 0 24 24"><path d="M2 11L22 2L15 22L11 13Z" fill="#fff"/></svg></div>
  <div class="c-label" style="left:689px;top:348px">Email</div>
  <div class="c-value" style="left:689px;top:370px">hello@brightharborguarding.biz</div>
  <div class="abs" style="left:0;top:522px;width:732px;height:58px;background:rgba(0,0,0,.55);clip-path:polygon(0 0,712px 0,732px 58px,0 58px)"></div>
  <div class="abs copyright">Copyright 2021. Brightharborguarding Firearms Training. All Rights Reserved.</div>
  <span class="social" style="left:903px" aria-label="Social link"></span>
  <span class="social" style="left:938px" aria-label="Social link"></span>
  <span class="social" style="left:973px" aria-label="Social link"></span>
  <span class="social" style="left:1008px" aria-label="Social link"></span>
</section>

</body>
</html>
```